New Business Card Design Project

I would like my card design to look exactly like the logo, design, layout, and print of the current attached file. The only change I would like made would be for the print to say THE KMR GROUP instead of THE MORALES GROUP. Basically, just replace his group name with my group name. I would also like the backgroud to be the same texture and color as the attached file. I love the dark blue lettering and house logo on the card.

I am completely open to the rest of the card design. I just want something clean and simple. Only basic contact info required on the card. Maybe just name: Wade K Holmer and cell # 555.014.2289 and email wade@thepxbroker.com

```html
<!DOCTYPE html>
<html lang="en">
<head>
<meta charset="utf-8">
<title>The KMR Group – Business Card</title>
<link rel="stylesheet" href="https://fonts.googleapis.com/css2?family=Montserrat:wght@300;400;700&display=swap">
<style>
  :root {
    --backdrop: #cfd3d3;
    --paper: #efefeb;
    --ink: #141b33;
    --card-shadow: rgba(40, 46, 50, 0.18);
  }
  * { box-sizing: border-box; margin: 0; padding: 0; }
  html, body {
    width: 1200px;
    height: 1050px;
    overflow: hidden;
    background: var(--backdrop);
  }
  .stage {
    width: 1200px;
    height: 1050px;
    display: flex;
    flex-direction: column;
    align-items: center;
    justify-content: center;
    gap: 70px;
  }
  .card {
    width: 595px;
    height: 340px;
    background: var(--paper);
    box-shadow: 0 6px 18px var(--card-shadow);
    color: var(--ink);
    font-family: "Montserrat", sans-serif;
    display: flex;
    align-items: center;
    justify-content: center;
  }
  .card--contact {
    flex-direction: column;
    text-align: center;
  }
  .contact__name {
    font-weight: 700;
    font-size: 24px;
    letter-spacing: 0.04em;
    margin-bottom: 26px;
  }
  .contact__line {
    font-weight: 400;
    font-size: 20px;
    letter-spacing: 0.05em;
    line-height: 1.3;
  }
  .card--brand { gap: 22px; }
  .brand__square {
    width: 78px;
    height: 78px;
    background: var(--ink);
  }
  .brand__name {
    font-weight: 300;
    font-size: 22px;
    letter-spacing: 0.16em;
    line-height: 1.18;
    text-transform: uppercase;
  }
  .brand__name span { display: block; }
</style>
</head>
<body>
  <main class="stage">
    <section class="card card--contact" aria-label="Card front">
      <p class="contact__name">Wade K Holmer</p>
      <p class="contact__line">555.014.2289</p>
      <p class="contact__line">wade@thepxbroker.com</p>
    </section>
    <section class="card card--brand" aria-label="Card back">
      <div class="brand__square" aria-hidden="true"></div>
      <p class="brand__name"><span>The</span><span>KMR</span><span>Group</span></p>
    </section>
  </main>
</body>
</html>
```